Enrollment Campaign

We need a flyer design for our school's enrollment campaign. Our school website is www.tbacademy.net.

The flyer should be double sided.

I want the reader to get the following messages:
1. Montessori graduates are leading the top companies of our time.
2. We are an accredited Montessori school.
3. Enrollment is open now for all four programs:
a) Toddler: 18months (or as soon as the child is able to walk) - 3 years
b) CASA: Preschool to Senior Kindergarten (3 years to 6 years)
c) Elementary: Grades 1 to 6
d) Junior High: Grades 7 to 8
4) Our contact information:
website, email:info@tbacademy.net, phone: 416 527 3962
5) Call for Action: Book a Tour! (there is a button on our website to book a tour)
6) In the languages punjabi, hindi and italian, I wouldn't readers to know that we offer their faith and cultural education as well.
7) Fees for children under age of 6 can be claimed in Taxes as day care expense. So, there is no reason to miss providing our children the best that we can in education.
Updates

Please note my updates to my brief in the "must have" section. Also, I have added some pics that can be used. Please note that I don't have one pic (the farming one referred to in my brief). I will really appreciate if you can kindly update your design accordingly.

Project Deadline Extended
Reason: Because of my recent update to the brief, some designers need some time to adjust their designs. I really appreciate your patience and kind consideration for my project. Thank you!

Industry/Entity Type

Education

Colors

Designer to choose colors to be used in the design.

Requirements
Must have
• Must have a unique design. I don't want a typical flyer. The design should be unique and memorable.

One of the main pics that I need is for illustrating a key feature of our new Junior High program that we are starting in August 2015. The key feature is that children are going to be operating a 'greenhouse', growing organic produce and will also be preparing their daily lunch from scratch. So, show a pic of a 13-14year old farming or something.

```html
<!DOCTYPE html>
<html lang="en">
<head>
<meta charset="utf-8">
<title>TB Academy – Enrollment Flyer</title>
<link rel="stylesheet" href="https://fonts.googleapis.com/css2?family=Didact+Gothic&family=Montserrat:wght@600;700&display=swap">
<style>
  :root {
    --olive: #6b7a3a;
    --olive-dark: #4f5b26;
    --olive-mid: #8e9b5c;
    --olive-light: #c5ccab;
    --olive-pale: #dfe3cf;
    --orange: #e8621c;
    --brown-text: #8a6a2a;
    --ink: #333333;
    --paper: #ffffff;
    --backdrop: #ffffff;
    --band-dark: #3d3a2c;
    --accent-lime: #c8d63a;
    --brand-blue: #3a8fcf;
  }
  * { box-sizing: border-box; margin: 0; padding: 0; }
  html, body { width: 1200px; height: 776px; overflow: hidden; background: var(--backdrop); }
  body { position: relative; font-family: "Didact Gothic", "Century Gothic", sans-serif; color: var(--ink); }
  h1, h2 { font-weight: 400; }
  .page { position: absolute; top: 4px; width: 588px; height: 766px; background: var(--paper); overflow: hidden; border: 1px solid #d8d8d8; }
  .page--front { left: 4px; }
  .page--back { left: 607px; }
  .abs { position: absolute; }
  .photo { position: absolute; }

  /* Front */
  .hero-photo { left: 0; top: 0; width: 588px; height: 400px; background: linear-gradient(160deg, #5d6b52 0%, #b9ab93 45%, #e9e1d4 100%); }
  .hero-curve { position: absolute; left: 0; top: 320px; width: 588px; height: 100px; }
  .front-brand { left: 405px; top: 150px; color: #fff; font-size: 27px; }
  .front-brand::before { content: ""; display: inline-block; width: 12px; height: 12px; border-radius: 50%; background: #fff; margin-right: 8px; vertical-align: middle; }
  .badge { left: 372px; top: 248px; width: 190px; height: 90px; background: rgba(255,255,255,.55); border-radius: 6px; }
  .boy-photo { left: 0; top: 420px; width: 226px; height: 207px; background: linear-gradient(135deg, #d7b08b, #9a7a62 60%, #6f7f94); }
  .front-heading { left: 233px; top: 432px; font-size: 31px; line-height: 38px; color: var(--orange); white-space: nowrap; }
  .front-sub { left: 233px; top: 470px; font-family: "Montserrat", sans-serif; font-weight: 700; font-size: 21px; line-height: 28px; color: var(--olive); white-space: nowrap; }
  .front-rule { left: 233px; top: 505px; width: 340px; height: 2px; background: var(--ink); }
  .quote { left: 233px; font-size: 14px; line-height: 18px; color: var(--ink); white-space: nowrap; }
  .quote cite { font-family: "Montserrat", sans-serif; font-weight: 700; font-style: italic; font-size: 9.5px; }
  .quote--one { top: 518px; }
  .quote--two { top: 539px; }
  .quote--three { top: 557px; }
  .front-para { left: 249px; top: 580px; font-size: 11.8px; line-height: 19px; color: var(--brown-text); white-space: nowrap; }
  .strip { top: 627px; height: 118px; }
  .strip--a { left: 0; width: 188px; background: linear-gradient(135deg, #d9c6a8, #7d5a3d); }
  .strip--b { left: 188px; width: 205px; background: linear-gradient(135deg, #6f8a3c, #b7c58a 60%, #e07a3d); }
  .strip--c { left: 393px; width: 195px; background: linear-gradient(135deg, #cfd7e0, #3958a5 50%, #d73a3a); }
  .front-foot { left: 0; top: 745px; width: 588px; height: 21px; background: var(--band-dark); }

  /* Back */
  .headline { left: 38px; top: 36px; color: var(--olive); white-space: nowrap; }
  .headline strong { display: block; font-family: "Montserrat", sans-serif; font-weight: 700; font-size: 29px; letter-spacing: .3px; line-height: 36px; }
  .headline span { display: block; font-size: 29px; line-height: 30px; }
  .accredit { left: 38px; top: 196px; font-size: 20px; color: var(--orange); line-height: 25px; white-space: nowrap; }
  .accredit b { font-family: "Montserrat", sans-serif; font-weight: 700; font-size: 18px; }
  .contact-bubble { left: 275px; top: 10px; width: 290px; height: 240px; }
  .contact { left: 318px; top: 48px; width: 235px; color: #5a5f45; }
  .contact h2 { font-size: 20px; line-height: 21px; text-align: center; color: var(--olive-dark); margin-bottom: 10px; }
  .contact li { list-style: none; font-size: 14.5px; line-height: 20px; display: flex; gap: 8px; white-space: nowrap; }
  .contact svg { flex: none; margin-top: 5px; }
  .gallery { top: 256px; height: 118px; }
  .gallery--1 { left: 43px; width: 101px; background: linear-gradient(135deg, #efe9de, #b6916a); }
  .gallery--2 { left: 146px; width: 101px; background: linear-gradient(135deg, #d9c4a6, #e0549a); }
  .gallery--3 { left: 249px; width: 101px; background: linear-gradient(135deg, #f1e0c3, #d95b3e); }
  .gallery--4 { left: 352px; width: 100px; background: linear-gradient(135deg, #cfd5db, #4d6aa3); }
  .gallery--5 { left: 454px; width: 94px; background: linear-gradient(135deg, #dde8d0, #e06e5d 55%, #3aa0c6); }
  .tour-ribbon { left: 34px; top: 392px; width: 330px; height: 88px; }
  .tour-title { left: 70px; top: 419px; font-family: "Montserrat", sans-serif; font-weight: 700; font-size: 30px; line-height: 36px; color: #fff; white-space: nowrap; }
  .tour-url { left: 70px; top: 457px; font-family: "Montserrat", sans-serif; font-weight: 700; font-size: 16px; line-height: 20px; color: var(--accent-lime); white-space: nowrap; }
  .language-note { left: 372px; top: 394px; width: 185px; font-size: 13.5px; line-height: 19px; color: var(--olive); }
  .language-note em { font-style: normal; color: var(--orange); }
  .enroll-title { left: 41px; top: 524px; font-family: "Montserrat", sans-serif; font-weight: 700; font-size: 19px; color: var(--olive); letter-spacing: .3px; white-space: nowrap; }
  .enroll-title span { font-weight: 400; font-family: "Didact Gothic", sans-serif; }
  .programs { left: 41px; top: 556px; width: 290px; border-collapse: collapse; }
  .programs th { width: 92px; background: var(--olive-mid); color: #fff; font-weight: 600; font-family: "Montserrat", sans-serif; font-size: 12px; text-align: left; padding: 0 8px; white-space: nowrap; }
  .programs td { background: var(--olive-light); color: #fff; font-size: 11.5px; line-height: 14px; padding: 0 8px; }
  .programs tr { height: 46px; }
  .programs tr + tr th, .programs tr + tr td { border-top: 1px dashed rgba(255,255,255,.8); }
  .divider { left: 350px; top: 524px; height: 230px; border-left: 3px dotted var(--olive-mid); }
  .class-photo { left: 368px; top: 522px; width: 178px; height: 118px; background: linear-gradient(135deg, #e3d8c6, #8f7a5b 55%, #3f6f8e); }
  .back-brand { left: 380px; top: 692px; font-size: 23px; color: var(--brand-blue); white-space: nowrap; }
  .back-brand::before { content: ""; display: inline-block; width: 11px; height: 11px; border-radius: 50%; background: var(--brand-blue); margin-right: 7px; vertical-align: middle; }
</style>
</head>
<body>

<section class="page page--front" aria-label="Flyer front">
  <div class="photo hero-photo" role="img" aria-label="Photo of a group of smiling schoolchildren lined up in front of a classroom chalkboard"></div>
  <svg class="hero-curve" viewBox="0 0 588 100" preserveAspectRatio="none" aria-hidden="true">
    <path d="M0 18 Q294 60 588 10 L588 100 L0 100 Z" fill="var(--olive)"/>
    <path d="M0 40 Q294 110 588 30 L588 100 L0 100 Z" fill="var(--paper)"/>
  </svg>
  <div class="abs front-brand">TB Academy</div>
  <div class="abs badge" aria-label="Accreditation badge"></div>

  <div class="photo boy-photo" role="img" aria-label="Photo of a smiling boy holding freshly picked carrots"></div>
  <h1 class="abs front-heading">Montessori Education</h1>
  <p class="abs front-sub">Toddlers to Grade 8</p>
  <div class="abs front-rule"></div>
  <p class="abs quote quote--one">"Montessori builds innovators" - <cite>Business Review Quarterly</cite></p>
  <p class="abs quote quote--two">"Montessori educational approach might be the surest</p>
  <p class="abs quote quote--three">route to joining the creative elite" - <cite>The Market Journal</cite></p>
  <p class="abs front-para">Success comes from a hands-on approach for real education,<br>encouraging risk taking, and a discipline for pursuing excellence.</p>

  <div class="photo strip strip--a" role="img" aria-label="Photo of students working at a classroom table"></div>
  <div class="photo strip strip--b" role="img" aria-label="Photo of children gardening in a vegetable patch"></div>
  <div class="photo strip strip--c" role="img" aria-label="Photo of two students using a microscope"></div>
  <div class="abs front-foot"></div>
</section>

<section class="page page--back" aria-label="Flyer back">
  <h2 class="abs headline">
    <strong>MONTESSORI</strong>
    <span>graduates are</span>
    <span>leading the top</span>
    <span>companies of</span>
    <span>our time</span>
  </h2>
  <p class="abs accredit"><b>CAMB Accredited</b><br>Montessori School</p>

  <svg class="abs contact-bubble" viewBox="0 0 290 240" aria-hidden="true">
    <path d="M160 8 C235 8 285 55 285 115 C285 180 230 225 160 225 C120 225 90 212 70 196 L8 228 L42 168 C35 152 32 134 32 115 C32 55 85 8 160 8 Z" fill="var(--olive-pale)"/>
  </svg>
  <div class="abs contact">
    <h2>Our Contact<br>Information</h2>
    <ul>
      <li><svg width="10" height="10" viewBox="0 0 10 10" aria-hidden="true"><circle cx="5" cy="5" r="4" fill="none" stroke="#5a5f45" stroke-width="1.5"/><circle cx="5" cy="5" r="1.5" fill="#5a5f45"/></svg>www.tbacademy.net</li>
      <li><svg width="10" height="8" viewBox="0 0 10 8" aria-hidden="true"><rect width="10" height="8" fill="#5a5f45"/><path d="M0 0 L5 4 L10 0" fill="none" stroke="#dfe3cf" stroke-width="1"/></svg>info@tbacademy.net</li>
      <li><svg width="10" height="10" viewBox="0 0 10 10" aria-hidden="true"><path d="M2 0 L4 0 L4.5 3 L3 4 Q4 6.5 6 7 L7 5.5 L10 6 L10 8 Q9 10 7 10 Q1 9 0 2 Q0 0 2 0 Z" fill="#5a5f45"/></svg>416-527-3962</li>
      <li><svg width="10" height="10" viewBox="0 0 10 10" aria-hidden="true"><path d="M5 0 L10 5 L8.5 5 L8.5 10 L6 10 L6 7 L4 7 L4 10 L1.5 10 L1.5 5 L0 5 Z" fill="#5a5f45"/></svg><span>7-2810 Maplewood Drive<br>Brampton, ON, L6R4K2</span></li>
    </ul>
  </div>

  <div class="photo gallery gallery--1" role="img" aria-label="Photo of a child in a turban working with Montessori cylinders"></div>
  <div class="photo gallery gallery--2" role="img" aria-label="Photo of a girl stacking a pink tower"></div>
  <div class="photo gallery gallery--3" role="img" aria-label="Photo of a toddler working with puzzle pieces"></div>
  <div class="photo gallery gallery--4" role="img" aria-label="Photo of a boy with glasses using a tablet"></div>
  <div class="photo gallery gallery--5" role="img" aria-label="Photo of a boy examining a globe with a magnifier"></div>

  <svg class="abs tour-ribbon" viewBox="0 0 330 88" aria-hidden="true">
    <path d="M0 8 L300 8 L300 84 L0 84 L22 46 Z" fill="var(--olive)"/>
    <path d="M296 0 L318 8 L300 8 Z" fill="var(--olive-dark)"/>
    <g transform="translate(262 34)" fill="none" stroke="var(--accent-lime)" stroke-width="2.5">
      <rect x="0" y="10" width="26" height="36" rx="13"/>
      <line x1="13" y1="10" x2="13" y2="24"/>
      <line x1="0" y1="24" x2="26" y2="24"/>
      <path d="M13 10 C13 0 26 4 22 -10"/>
    </g>
  </svg>
  <p class="abs tour-title">Book a Tour</p>
  <p class="abs tour-url">www.tbacademy.net</p>
  <p class="abs language-note">French language learning begins in CASA. Optional ethnic language and faith programs are provided. <em>We welcome all faiths and cultures.</em></p>

  <h2 class="abs enroll-title">ENROLLMENT <span>IS</span> OPEN NOW</h2>
  <table class="abs programs">
    <tr><th>Toddler</th><td>18months (or as soon as the child is able to walk) ~ 3 years</td></tr>
    <tr><th>CASA</th><td>Preschool to Senior Kindergarten (3 years to 6 years)</td></tr>
    <tr><th>Elementary</th><td>Grades 1 to 6</td></tr>
    <tr><th>Junior High</th><td>Grades 7 to 8</td></tr>
  </table>
  <div class="abs divider"></div>
  <div class="photo class-photo" role="img" aria-label="Photo of a teacher guiding students at a classroom table"></div>
  <div class="abs back-brand">TB Academy</div>
</section>

</body>
</html>
```